New business card for Building services company

I own a small 1 person business which primarily works at heights. I gain access to my work areas via ladders and use safety harnesses. I conduct gutter cleaning, roof cleaning with a pressure cleaner(water blaster), ground level pressure cleaning (driveways, footpaths and walls), I also do small handy-man jobs & gardening/ tree trimming.

I have just had a logo designed by Sketch Hive, which I will upload. I'd like to see the themes followed through.
I like the colour of aqua or the colours what is in the logo.

I live in tropical north Queensland in Cairns, Australia. It is where the rain forest meets the Coral Lantern Shoal. On average it is 30+ degrees C.
Updates

Hello all designers. Thankyou for all the submissions so far. The following are my business details which I need on the card-

VERNO Roof, Gutter & Pressure Cleaning Services.
Director -Dale Marwick
Ph 0417385026
Email- roofcleaning@plovernet.example.au
ABN -48 902 317 254

Please include the following services which my business conducts-
*Gutter Cleaning
*Pressure Cleaning- Roof's, Driveways etc
*Minor Roof, Gutter & Building Maintenance
*Garden waste removal & complex cleanups

Public Liability upto $10 Million
Working at Heights Cert.

Quote-                                     Date-

Hi everyone,  could you please ensure you have -"Quote" and "Date" on the card. I'll need space to hand write details on the card for the specific details.        

Requirements
Must have
• The logo attached must be included.
• The rear side of the card is dedicated to job quoted and price of the job.
• *Please include- Quote price, Quote date. etc
• Including the tasks I do at work around the side of the card- Gutter Cleaning; Roof Cleaning, Gutter Maintenance; Gardening; Pressure Cleaning Roof's, Driveways etc.
Nice to have
• The rear side to have a ladder

```html
<!DOCTYPE html>
<html lang="en">
<head>
<meta charset="utf-8">
<title>VERNO Business Card</title>
<link href="https://fonts.googleapis.com/css2?family=Questrial&display=swap" rel="stylesheet">
<style>
  :root {
    --navy: #2a2f8f;
    --royal: #2b3aa8;
    --teal: #17a89a;
    --aqua: #2ec4b0;
    --card: #fbfbfc;
    --stage: #ffffff;
    --edge: #e3e4ea;
  }
  * { margin: 0; padding: 0; box-sizing: border-box; }
  html, body { width: 1200px; height: 900px; overflow: hidden; background: var(--stage); }
  body { font-family: "Questrial", "Century Gothic", sans-serif; position: relative; }

  .card {
    position: absolute;
    top: 280px;
    width: 560px;
    height: 375px;
    background: var(--card);
    border: 1px solid var(--edge);
    border-radius: 26px;
    overflow: hidden;
  }
  .card--front { left: 30px; }
  .card--back { left: 610px; }

  /* Front */
  .brand { position: absolute; left: 32px; top: 70px; display: flex; align-items: center; gap: 16px; }
  .brand__mark { width: 26px; height: 26px; border-radius: 50%; background: var(--teal); }
  .brand__name { font-size: 76px; color: var(--royal); letter-spacing: 2px; line-height: 1; }
  .brand__services {
    position: absolute; left: 32px; top: 150px;
    font-size: 12.5px; color: var(--royal); letter-spacing: 0.4px; text-transform: uppercase;
  }
  .band { position: absolute; left: 0; right: 0; top: 178px; }
  .band__blue { height: 7px; background: var(--royal); }
  .band__teal { height: 9px; background: linear-gradient(90deg, var(--teal), var(--aqua)); }

  .person { position: absolute; left: 30px; top: 200px; }
  .person__name { font-size: 17px; color: var(--teal); }
  .person__role { font-size: 13px; color: var(--navy); margin-top: 3px; }

  .contact { position: absolute; left: 30px; top: 252px; color: var(--navy); }
  .contact__line { display: flex; align-items: center; gap: 5px; font-size: 17px; line-height: 24px; }
  .contact__icon { width: 15px; height: 15px; flex: none; }
  .contact__abn { font-size: 12px; margin: 3px 0 0 20px; }

  /* Back */
  .services { position: absolute; left: 38px; top: 48px; list-style: none; color: var(--navy); }
  .services li { font-size: 17.5px; line-height: 25px; }
  .services li::before { content: "* "; color: var(--teal); }

  .credentials { position: absolute; left: 40px; top: 175px; color: var(--teal); font-size: 16.5px; line-height: 24px; }

  .field { position: absolute; left: 40px; display: flex; align-items: center; color: var(--navy); font-size: 17px; }
  .field--quote { top: 225px; }
  .field--date { top: 272px; }
  .field__label { width: 62px; }
  .field__box { height: 31px; border: 2px solid var(--teal); background: #fff; }
  .field--quote .field__box { width: 415px; }
  .field--date .field__box { width: 208px; }
</style>
</head>
<body>

  <section class="card card--front" aria-label="Card front">
    <div class="brand">
      <span class="brand__mark"></span>
      <span class="brand__name">VERNO</span>
    </div>
    <p class="brand__services">Roof, Gutter &amp; Pressure Cleaning Services</p>
    <div class="band"><div class="band__blue"></div><div class="band__teal"></div></div>

    <div class="person">
      <p class="person__name">Dale Marwick</p>
      <p class="person__role">Director</p>
    </div>

    <div class="contact">
      <p class="contact__line">
        <svg class="contact__icon" viewBox="0 0 24 24"><path fill="#17a89a" d="M6.6 10.8a15.1 15.1 0 0 0 6.6 6.6l2.2-2.2c.3-.3.7-.4 1-.2 1.1.4 2.3.6 3.6.6.6 0 1 .4 1 1V20c0 .6-.4 1-1 1A17 17 0 0 1 3 4c0-.6.4-1 1-1h3.5c.6 0 1 .4 1 1 0 1.3.2 2.5.6 3.6.1.3 0 .7-.2 1z"/></svg>
        0417385026
      </p>
      <p class="contact__line">
        <svg class="contact__icon" viewBox="0 0 24 24"><rect x="2" y="5" width="20" height="14" rx="2" fill="#17a89a"/><path d="M3 6l9 7 9-7" fill="none" stroke="#fff" stroke-width="2"/></svg>
        roofcleaning@plovernet.example.au
      </p>
      <p class="contact__abn">ABN -48 902 317 254</p>
    </div>
  </section>

  <section class="card card--back" aria-label="Card back">
    <ul class="services">
      <li>Gutter Cleaning</li>
      <li>Pressure Cleaning- Roof's, Driveways etc</li>
      <li>Minor Roof, Gutter &amp; Building Maintenance</li>
      <li>Garden waste removal &amp; complex cleanups</li>
    </ul>

    <div class="credentials">
      <p>Public Liability upto $10 Million</p>
      <p>Working at Heights Cert.</p>
    </div>

    <div class="field field--quote"><span class="field__label">Quote-</span><span class="field__box"></span></div>
    <div class="field field--date"><span class="field__label">Date-</span><span class="field__box"></span></div>
  </section>

</body>
</html>
```